Landscape design build company door flyer

I would like this flyer to convey a high-level of professionalism for a company that is excellent with communication with their clients as well as a company that does incredible installations

Went on vacation/holiday

```html
<!DOCTYPE html>
<html lang="en">
<head>
<meta charset="utf-8">
<title>Harbor Stone Builders – Door Hangers</title>
<link href="https://fonts.googleapis.com/css2?family=Poppins:wght@500;600;700;800&display=swap" rel="stylesheet">
<style>
:root{
  --navy:#12354a;
  --gold:#fbb316;
  --page:#f1f1f3;
  --white:#ffffff;
  --ink:#0f2c3d;
}
*{margin:0;padding:0;box-sizing:border-box}
html,body{width:1200px;height:1200px;overflow:hidden;background:var(--page)}
body{position:relative;font-family:'Poppins',sans-serif;color:var(--ink)}
.hanger{position:absolute;top:160px;width:342px;height:880px;border-radius:18px;overflow:hidden;background:var(--white)}
.hanger--front{left:173px}
.hanger--back{left:687px}
.abs{position:absolute}
.center{text-align:center}
.cutout{position:absolute;left:0;top:0;width:342px;height:230px;pointer-events:none;z-index:5}

/* front */
.hero-photo{left:0;top:0;width:342px;height:345px;background:linear-gradient(180deg,#8aa54b 0%,#a7a39a 22%,#6b5442 40%,#8f8a82 62%,#bfbcb6 80%,#ffffff 100%)}
.brand{left:0;width:342px;top:292px}
.brand__name{font-weight:600;font-size:22px;letter-spacing:.3px;color:var(--navy);line-height:1}
.brand__tag{font-weight:500;font-size:11px;color:var(--navy);margin-top:4px;line-height:1}
.headline-band{left:0;top:342px;width:342px;height:200px;background:var(--navy)}
.headline{left:0;top:348px;width:342px;color:var(--white);font-weight:800;font-size:36px;line-height:47px}
.pill{background:var(--gold);color:var(--navy);font-weight:600;border-radius:30px;display:flex;align-items:center;justify-content:center;text-align:center;z-index:3}
.pill--intro{left:32px;top:495px;width:276px;height:60px;font-size:14px;line-height:18px}
.services-area{left:0;top:540px;width:342px;height:250px;background:linear-gradient(180deg,#e7e6e2,#ffffff 35%,#ffffff)}
.services-title{left:0;top:564px;width:342px;display:flex;align-items:center;justify-content:center;gap:10px;font-weight:700;font-size:20px;color:var(--navy)}
.services-title::before,.services-title::after{content:"";display:block;width:100px;height:2px;background:var(--navy)}
.services-list{left:8px;top:598px;width:326px;font-weight:700;font-size:14px;line-height:18px;color:var(--navy)}
.thumb{top:668px;width:97px;height:66px;border-radius:6px}
.thumb--1{left:12px;background:linear-gradient(160deg,#8e8a83,#a38a67 60%,#6e655c)}
.thumb--2{left:122px;background:linear-gradient(170deg,#a9b2b7,#6f8151 55%,#8d857a)}
.thumb--3{left:231px;background:linear-gradient(150deg,#7a5444,#5c3a2e 60%,#8a6655)}
.footer-band{left:0;top:778px;width:342px;height:102px;background:var(--navy)}
.pill--cta{left:36px;top:755px;width:268px;height:48px;font-size:13px;line-height:16px}
.phone{height:25px;border-radius:13px;background:var(--gold);color:var(--navy);font-weight:700;font-size:12px;display:flex;align-items:center;gap:3px;padding:0 8px 0 3px}
.phone svg{width:19px;height:19px}
.email{display:flex;align-items:center;gap:5px;color:var(--white);font-weight:500;font-size:8px}
.email svg{width:11px;height:8px}
.address{color:var(--white);font-weight:600;font-size:9.5px;line-height:12px}
.divider{width:1px;background:var(--gold)}

/* back */
.back-photo{left:0;top:0;width:342px;height:240px;background:linear-gradient(180deg,#6a7d41 0%,#9b6d3f 20%,#5a5754 48%,#3b4a52 75%,var(--navy) 100%)}
.back-navy{left:0;top:238px;width:342px;height:150px;background:var(--navy)}
.serving{left:0;top:234px;width:342px;color:var(--white);font-weight:700;font-size:18px;line-height:23px}
.pill--area{left:31px;top:300px;width:280px;height:89px;border-radius:45px;font-size:12px;line-height:14.5px;padding:0 20px}
.values-area{left:0;top:385px;width:342px;height:378px;background:linear-gradient(180deg,#dfe3e6,#f4f5f6 30%,#ffffff 60%)}
.value{top:413px;width:110px;text-align:center}
.value svg{width:62px;height:62px;display:block;margin:0 auto 10px}
.value__label{font-weight:800;font-size:11.5px;line-height:14px;color:var(--navy)}
.reviews{left:10px;top:537px;width:320px;height:214px;border:2px solid var(--navy);border-radius:22px}
.reviews__title{left:76px;top:524px;width:190px;height:22px;background:var(--navy);border-radius:11px;color:var(--gold);font-weight:800;font-size:13px;display:flex;align-items:center;justify-content:center}
.stars{left:0;top:546px;width:342px;color:var(--gold);font-size:17px;letter-spacing:3px;line-height:18px}
.review{top:572px;width:140px;text-align:center;font-weight:500;font-size:8.2px;line-height:10.6px;color:var(--ink)}
.review__name{font-weight:700;margin-top:5px}
.review--a{left:19px}
.review--b{left:180px}
.reviews__rule{left:170px;top:576px;height:164px;width:1px;background:var(--navy)}
.back-footer{left:0;top:762px;width:342px;height:118px;background:var(--navy)}
.back-cta{left:0;top:769px;width:342px;color:var(--gold);font-weight:600;font-size:13px;line-height:16px}
.gold-rule{left:0;top:809px;width:342px;height:2px;background:var(--gold)}
.back-brand{left:250px;top:842px;width:86px;color:var(--white);text-align:center;line-height:1}
.back-brand__name{font-weight:600;font-size:8px}
.back-brand__tag{font-weight:500;font-size:4.5px;margin-top:2px}
</style>
</head>
<body>

<!-- FRONT -->
<section class="hanger hanger--front">
  <div class="abs hero-photo" role="img" aria-label="Photo of a covered backyard patio with stone fireplace, timber posts and outdoor seating"></div>
  <div class="abs brand center">
    <div class="brand__name">HARBOR STONE BUILDERS</div>
    <div class="brand__tag">OUTDOOR LIVING SPACES</div>
  </div>
  <div class="abs services-area" role="img" aria-label="Faded photo of a backyard pavilion behind the services list"></div>
  <div class="abs headline-band"></div>
  <h1 class="abs headline center">Ready to<br>Discover your<br>Zen?</h1>
  <div class="abs pill pill--intro">From vision to reality, We bring<br>your dream outdoor space to life.</div>
  <h2 class="abs services-title">Services</h2>
  <p class="abs services-list center">Paver Patios • Paver Driveways • Retaining Walls • Decks &amp; Railings &nbsp;• Pools • Outdoor Lighting &nbsp;• Firepits and Fireplaces</p>
  <div class="abs thumb thumb--1" role="img" aria-label="Photo of a stone seating wall with timber bench"></div>
  <div class="abs thumb thumb--2" role="img" aria-label="Photo of a retaining wall with garden planting"></div>
  <div class="abs thumb thumb--3" role="img" aria-label="Photo of a timber deck surface"></div>
  <div class="abs footer-band"></div>
  <div class="abs pill pill--cta">Contact us today for a consultation<br>and let's bring your vision to reality.</div>
  <div class="abs phone" style="left:15px;top:825px">
    <svg viewBox="0 0 20 20"><circle cx="10" cy="10" r="8.5" fill="none" stroke="#12354a" stroke-width="1.6"/><path d="M7 5.5l1.6 2.2-1 1.2c.6 1.3 1.5 2.2 2.8 2.8l1.2-1 2.2 1.6-.8 1.7c-3.6-.3-6.6-3.3-6.9-6.9z" fill="#12354a"/></svg>
    (206) 555-0148
  </div>
  <div class="abs email" style="left:18px;top:858px">
    <svg viewBox="0 0 11 8"><rect x=".5" y=".5" width="10" height="7" fill="none" stroke="#fff"/><path d="M.5.5l5 4 5-4" fill="none" stroke="#fff"/></svg>
    info@harborstonebuilders.com
  </div>
  <div class="abs divider" style="left:179px;top:820px;height:52px"></div>
  <svg class="abs" style="left:201px;top:834px" width="22" height="26" viewBox="0 0 22 26"><path d="M11 2a7 7 0 0 1 7 7c0 5-7 11-7 11S4 14 4 9a7 7 0 0 1 7-7z" fill="none" stroke="#fbb316" stroke-width="1.6"/><circle cx="11" cy="9" r="2.5" fill="none" stroke="#fbb316" stroke-width="1.6"/><ellipse cx="11" cy="22.5" rx="8" ry="2" fill="none" stroke="#fbb316" stroke-width="1.4"/></svg>
  <p class="abs address" style="left:230px;top:829px">18220 NE 4th St,<br>Sammamish, WA<br>98074</p>
  <svg class="cutout" viewBox="0 0 342 230"><g fill="var(--page)"><circle cx="184" cy="112" r="55"/><rect x="184" y="123" width="160" height="47"/><path d="M342 93V123H312Q342 123 342 93Z"/><path d="M342 170V200Q342 170 312 170Z"/></g></svg>
</section>

<!-- BACK -->
<section class="hanger hanger--back">
  <div class="abs back-photo" role="img" aria-label="Photo of a paver patio beside a timber fence and ornamental grasses"></div>
  <div class="abs values-area" role="img" aria-label="Faded photo of a backyard pavilion behind the values and reviews"></div>
  <div class="abs back-navy"></div>
  <h2 class="abs serving center">Proudly Serving Clients in and<br>around Seattle Since 2018</h2>
  <div class="abs pill pill--area">Headquartered in Sammamish, we typically consider projects in Eastside Seattle, including the areas of Bellevue, Issaquah, Kirkland, Redmond, and Sammamish</div>

  <div class="abs value" style="left:7px">
    <svg viewBox="0 0 62 62" fill="none" stroke="#12354a" stroke-width="2"><path d="M18 55V44c-6-4-9-10-9-17a21 21 0 0 1 42 0l4 8-5 1v7c0 3-2 5-5 5h-5v7"/><circle cx="30" cy="27" r="12"/><path d="M41 36l7 7"/><path d="M24 25h12l-6 8z M26 21h8l2 4H24z"/></svg>
    <div class="value__label">Distinctive<br>Design</div>
  </div>
  <div class="abs value" style="left:113px">
    <svg viewBox="0 0 62 62" fill="none" stroke="#12354a" stroke-width="2"><path d="M12 18l6-6 30 30 2 8-8-2z"/><path d="M50 12a7 7 0 0 0-9 9L14 48a4 4 0 0 0 6 6l27-27a7 7 0 0 0 9-9l-4 4-5-1-1-5z"/></svg>
    <div class="value__label">Uncompromising<br>Craftsmanship</div>
  </div>
  <div class="abs value" style="left:219px">
    <svg viewBox="0 0 62 62" fill="none" stroke="#12354a" stroke-width="2"><path d="M31 8l3 6 6 1-4 4 1 6-6-3-6 3 1-6-4-4 6-1z"/><path d="M16 14l2 4 4 .5-3 3 .8 4-3.8-2-3.8 2 .8-4-3-3 4-.5z"/><path d="M46 14l2 4 4 .5-3 3 .8 4-3.8-2-3.8 2 .8-4-3-3 4-.5z"/><path d="M6 44h8l8-4h10a3 3 0 0 1 0 6h-8 10l14-6a3 3 0 0 1 3 5L37 54H14"/><rect x="2" y="42" width="5" height="14"/></svg>
    <div class="value__label">Exceptional<br>Service</div>
  </div>

  <div class="abs reviews"></div>
  <div class="abs reviews__title">What Our Clients Say</div>
  <div class="abs stars center">★★★★★</div>
  <div class="abs reviews__rule"></div>
  <div class="abs review review--a">"Marcus from Harbor Stone Builders is a magician! There is no other way to explain the transformation of our yard!!! With an incredible attention to detail and a comprehensive vision of how to transform and elevate our outdoor space I can wholeheartedly recommend hiring Harbor Stone Builders. Our project may not have been his biggest, but Marcus gave us his undivided attention and took care of our every request"<div class="review__name">- RENATA F.</div></div>
  <div class="abs review review--b">"Marcus and his team were really great to work with!! Responsive and they started right away once we gave the go. He answered all our questions and worked with us all along the way through our project. Our hard scape turned out amazing and really transformed our house and curb appeal. Our neighbors keep reaching out to get his contact so if you're on the fence about your project I would reach out sooner than later!!" our every request"<div class="review__name">- DANA M.</div></div>

  <div class="abs back-footer"></div>
  <p class="abs back-cta center">Contact us today for a consultation<br>and let's bring your vision to reality.</p>
  <div class="abs gold-rule"></div>
  <div class="abs phone" style="left:8px;top:828px">
    <svg viewBox="0 0 20 20"><circle cx="10" cy="10" r="8.5" fill="none" stroke="#12354a" stroke-width="1.6"/><path d="M7 5.5l1.6 2.2-1 1.2c.6 1.3 1.5 2.2 2.8 2.8l1.2-1 2.2 1.6-.8 1.7c-3.6-.3-6.6-3.3-6.9-6.9z" fill="#12354a"/></svg>
    (206) 555-0148
  </div>
  <div class="abs email" style="left:10px;top:862px">
    <svg viewBox="0 0 11 8"><rect x=".5" y=".5" width="10" height="7" fill="none" stroke="#fff"/><path d="M.5.5l5 4 5-4" fill="none" stroke="#fff"/></svg>
    info@harborstonebuilders.com
  </div>
  <svg class="abs" style="left:189px;top:820px" width="14" height="17" viewBox="0 0 22 26"><path d="M11 2a7 7 0 0 1 7 7c0 5-7 11-7 11S4 14 4 9a7 7 0 0 1 7-7z" fill="none" stroke="#fbb316" stroke-width="2"/><circle cx="11" cy="9" r="2.5" fill="none" stroke="#fbb316" stroke-width="2"/><ellipse cx="11" cy="22.5" rx="8" ry="2" fill="none" stroke="#fbb316" stroke-width="1.8"/></svg>
  <p class="abs address center" style="left:141px;top:840px;width:110px;font-size:9px;line-height:11px">18220 NE 4th St,<br>Sammamish, WA<br>98074</p>
  <div class="abs back-brand">
    <div class="back-brand__name">HARBOR STONE BUILDERS</div>
    <div class="back-brand__tag">OUTDOOR LIVING SPACES</div>
  </div>
  <svg class="cutout" viewBox="0 0 342 230"><g fill="var(--page)"><circle cx="170" cy="112" r="55"/><rect x="170" y="123" width="174" height="47"/><path d="M342 93V123H312Q342 123 342 93Z"/><path d="M342 170V200Q342 170 312 170Z"/></g></svg>
</section>

</body>
</html>
```